Corporate flyer highlighting service offering for PR agency

A corporate flyer is needed for a new service offering that we are doing. The product name is SaleWise it is a marketing and communications services offering for companies who are getting ready to sell their business. If we are really happy with the designer's work, there will be a great deal more projects. I am looking for a clean design with a few pops of color from my site. https://brightlarkmoor.partners. I am looking for a good design with data in sections. I am looking for a clean design that feels high-end but not cluttered. Please do not use images of people. Please see the following examples of types of designs I like.
https://www.pinspotboard.com/pin/508213746120394861/
https://www.pinspotboard.com/pin/371920465837201548/
https://assets.lomvira.com/corporate-flyer-template-KPTRXB
https://artbazaro.net/item/corporate-flyer-template/48193067?s_rank=8
https://assets.lomvira.com/corporate-business-flyer-template-93BQMZ

I had to place the project on hold as I choose the wrong type of project and did not get many designs as a result. I am reposting this with an updated brief.

Target Market(s)

Business sellers and brokers

Industry/Entity Type

Marketing for business sellers

Font styles to use
Sans Serif

Requirements
Must have
• Good quality design with content in sections. Clean and high end feeling is a must.
Should not have
• A lot of images of people.

```html
<!DOCTYPE html>
<html lang="en">
<head>
<meta charset="utf-8">
<title>SaleWise Flyer</title>
<link href="https://fonts.googleapis.com/css2?family=Montserrat:wght@400;600;700&family=Open+Sans:ital,wght@0,400;0,600;0,700;1,400;1,600&display=swap" rel="stylesheet">
<style>
:root{
  --blue:#1f6cb5;--blue-lt:#3c8fd8;--blue-pale:#cfe5f7;--green:#5c9e2e;--green-lt:#8cc43f;
  --orange:#e8901c;--ink:#2e2e2e;--grey:#6d6d6d;--bg:#e6e6e4;--white:#fff;
}
*{margin:0;padding:0;box-sizing:border-box}
html,body{width:840px;height:1200px;overflow:hidden;background:var(--bg)}
body{position:relative;font-family:"Open Sans",Arial,sans-serif;color:var(--ink)}
.page{position:absolute;width:390px;height:552px;background:var(--white);overflow:hidden;box-shadow:0 2px 6px rgba(0,0,0,.18)}
.p1{left:20px;top:32px}.p2{left:430px;top:32px}.p3{left:20px;top:616px}.p4{left:430px;top:616px}
.abs{position:absolute}
svg.layer{position:absolute;left:0;top:0}
.body{font-size:5.2px;line-height:1.45;color:#555}
.brand{display:flex;align-items:center;gap:5px;font-family:"Montserrat",sans-serif;font-weight:600;color:var(--ink);letter-spacing:.3px;white-space:nowrap}
.brand .mark{width:10px;height:10px;background:var(--blue);flex:none}
.headline{font-family:"Montserrat",sans-serif;font-weight:700;color:var(--ink);text-align:right;line-height:1.02}
.url{font-family:"Montserrat",sans-serif;color:#fff;font-size:8px;white-space:nowrap}
.sec-h{font-family:"Montserrat",sans-serif;font-weight:600;font-size:6.4px;color:var(--ink);text-transform:uppercase;line-height:1.2;padding-left:22px;position:relative}
.sec-h::before{content:"";position:absolute;left:0;top:0;width:0;height:0;border-left:16px solid var(--green);border-top:14px solid transparent}
.bul{list-style:none}
.bul li{position:relative;padding-left:10px;margin-top:5px}
.bul li::before{content:"";position:absolute;left:1px;top:2px;width:4px;height:4px;border-radius:50%;background:var(--blue)}
.bul b{color:var(--blue);font-weight:600}
.step{position:absolute;height:22px;background:var(--blue-pale);font-size:7.2px;display:flex;align-items:center;color:var(--ink)}
.step.alt{background:#fff}
.num{position:absolute;width:20px;height:20px;border-radius:50%;background:#fff;border:2px solid var(--blue);color:var(--blue);font-family:"Montserrat",sans-serif;font-weight:700;font-size:10px;display:flex;align-items:center;justify-content:center}
.hex{position:absolute;width:42px;height:38px;clip-path:polygon(25% 0,75% 0,100% 50%,75% 100%,25% 100%,0 50%);display:flex;align-items:flex-end;justify-content:center;padding-bottom:6px;color:#fff;font-size:3.6px;font-weight:600;text-align:center;line-height:1.1}
.hex.g{background:var(--green)}.hex.b{background:var(--blue)}
</style>
</head>
<body>

<!-- Page 1 -->
<section class="page p1">
  <svg class="layer" width="390" height="552" viewBox="0 0 390 552">
    <g role="img" aria-label="Photo of glass office building facades in blue and green tones">
      <polygon points="0,0 95,0 48,90 0,90" fill="#3a7fc2"/>
      <polygon points="70,0 160,0 115,85" fill="#2c6aa8"/>
      <polygon points="0,95 50,95 140,95 95,180 0,180" fill="#4f9a2f"/>
      <polygon points="100,95 170,95 135,160" fill="#7fb947"/>
      <polygon points="0,185 90,185 45,250 0,250" fill="#3f8cd0"/>
      <polygon points="95,185 160,185 128,240" fill="#5fa83a"/>
    </g>
    <polygon points="150,0 210,0 120,170" fill="#1f6cb5" opacity=".85"/>
    <polygon points="205,235 390,235 390,300 175,300" fill="#1f6cb5"/>
    <polygon points="0,532 390,516 390,552 0,552" fill="#1f6cb5"/>
    <polygon points="230,320 390,320 390,470 250,470" fill="#e8901c"/>
  </svg>
  <div class="abs brand" style="left:222px;top:32px;font-size:8.5px"><span class="mark"></span>BRIGHTLARKMOOR PARTNERS</div>
  <div class="abs headline" style="right:22px;top:110px;font-size:34px">SALE<br>WISE</div>
  <div class="abs" style="left:215px;top:244px;color:#fff">
    <div style="font-family:Montserrat,sans-serif;font-weight:700;font-size:15px">SaleWise</div>
    <div style="font-size:5.6px;font-weight:600;text-align:center;margin-top:4px;width:160px;line-height:1.35">provides executives and business owners with clear guidance to unlock non-financial value ahead of an exit.</div>
  </div>
  <div class="abs body" style="left:24px;top:262px;width:130px">
    <p>A strong communication and marketing strategy can significantly increase the value of your business leading up to an exit. Buyers are looking to mitigate risk and unlock potential value as a catalyst for clear growth potential.</p>
    <p style="margin-top:6px">Highlighting your company's success in the marketplace, identifying and mitigating reputation risks before buyers do, enhancing employee engagement, finding hidden opportunities to boost marketing KPIs and showcasing IP, data and innovation can make a significant difference in valuation.</p>
    <p style="margin-top:6px;font-style:italic;font-weight:600;color:#333;width:200px">We design and implement communication and marketing strategies that deliver significant increases in brand awareness, identify reputational risks, and enhance brand perception, helping owners and investors to realize premium values for their companies. We support owners and companies through:</p>
  </div>
  <div class="abs" style="left:258px;top:334px;width:118px;color:#fff;font-size:5.6px;font-style:italic;font-weight:600;line-height:1.4;text-align:center">US institutional investors believe that Investor Relations (IR) accounts for a total variance of 30% in a company's valuation – from a premium of 10% for "superb" IR to a discount of 20% for "poor" IR. —Corvane Research Group, "Harnessing IR's Power to Impact a Company's Valuation."</div>
  <div class="hex g" style="left:26px;top:418px">COMPANY EXIT PREPARATION</div>
  <div class="hex b" style="left:68px;top:440px">M&amp;A</div>
  <div class="hex g" style="left:110px;top:418px">IPO</div>
  <div class="hex b" style="left:152px;top:440px">SPINOFF/ DIVESTITURE</div>
  <div class="hex g" style="left:194px;top:418px">NEW LEADERSHIP/ INVESTOR</div>
  <div class="abs body" style="left:18px;top:488px;width:330px">Few sellers would list their home without first inspecting, repairing broken items, and making updates to highlight the positive aspects – increasing appeal to buyers. However, countless business owners leave money on the table during corporate exits due to a lack of preparation.</div>
  <div class="abs url" style="left:128px;top:537px">www.brightlarkmoor.partners</div>
</section>

<!-- Page 2 -->
<section class="page p2">
  <svg class="layer" width="390" height="552" viewBox="0 0 390 552">
    <polygon points="210,20 390,20 390,160 170,160" fill="#6fae3a" role="img" aria-label="Photo of a rising green financial bar chart"/>
    <polygon points="195,0 225,0 130,160 110,160" fill="#fff"/>
    <polygon points="0,140 55,140 0,200" fill="#e8901c"/>
    <polygon points="330,140 390,140 390,300" fill="#e8901c"/>
    <rect x="0" y="160" width="390" height="152" fill="#1f6cb5"/>
    <rect x="0" y="160" width="190" height="152" fill="#2f7fc6" role="img" aria-label="Photo of a hand using a calculator over financial papers"/>
    <polygon points="0,470 70,552 0,552" fill="#1f6cb5"/>
    <polygon points="0,490 30,552 0,552" fill="#3c8fd8"/>
    <polygon points="360,470 390,470 390,552 340,552" fill="#1f6cb5"/>
  </svg>
  <div class="abs body" style="left:24px;top:38px;width:240px">Our team of executive-level communications and marketing experts brings deep buy and sell-side experience. We have played critical roles in the acquisition, integration, and disposition process. Our mix of financial services expertise combined with decades of experience leading internal and external communications, marketing and investor relations teams gives us a unique perspective on identifying and unlocking non-financial areas of value and mitigating non-financial risks before exit.</div>
  <div class="abs" style="left:192px;top:182px;width:176px;color:#fff;font-size:7px;font-style:italic;line-height:1.4;text-align:justify">While accounting and investment banking teams are hard at work increasing value from a financial perspective, we help organizations enhance their valuation by identifying areas that will appeal most to buyers and ensuring those elements of your business are visible and memorable to those who matter most.</div>
  <div class="abs" style="left:28px;top:328px;font-family:Montserrat,sans-serif;font-weight:600;font-size:9.5px">WE HELP COMPANIES INCREASE VALUATION BY:</div>
  <svg class="layer" width="390" height="552" viewBox="0 0 390 552">
    <polygon points="118,352 140,352 92,452 70,452" fill="#5c9e2e"/>
  </svg>
  <div class="step" style="left:140px;top:364px;width:250px;padding-left:14px">Highlighting value in a clear and visible way</div>
  <div class="step alt" style="left:118px;top:394px;width:272px;padding-left:22px">Streamlining the exit process</div>
  <div class="step" style="left:98px;top:424px;width:292px;padding-left:18px">Identifying potential risks and suggesting mitigation measures</div>
  <div class="step alt" style="left:78px;top:454px;width:312px;padding-left:16px">Creating a polished presence in the market ahead of buyer interest</div>
  <div class="num" style="left:118px;top:356px">1</div>
  <div class="num" style="left:98px;top:386px">2</div>
  <div class="num" style="left:78px;top:416px">3</div>
  <div class="num" style="left:52px;top:452px">4</div>
  <div class="abs brand" style="left:62px;top:521px;font-size:6.5px"><span class="mark" style="width:8px;height:8px"></span>BRIGHTLARKMOOR PARTNERS</div>
  <div class="abs" style="left:205px;top:516px;width:185px;height:16px;background:#6d6d6d"></div>
  <div class="abs url" style="left:222px;top:519px">www.brightlarkmoor.partners</div>
</section>

<!-- Page 3 -->
<section class="page p3">
  <svg class="layer" width="390" height="552" viewBox="0 0 390 552">
    <polygon points="0,12 375,12 350,50 0,50" fill="#1f6cb5"/>
    <polygon points="0,535 390,520 390,552 0,552" fill="#1f6cb5"/>
    <rect x="30" y="320" width="150" height="128" fill="#e8901c"/>
  </svg>
  <div class="abs" style="left:18px;top:20px;width:340px;color:#fff;font-size:5.8px;font-weight:600;line-height:1.35">SaleWise provides executives and business owners with clear guidance to unlock value ahead of an exit. Our non-disruptive, ala-carte process enables us to work with sellers on specific areas or to do a complete analysis and recommendation and can include:</div>
  <div class="abs body" style="left:14px;top:62px;width:172px">
    <div class="sec-h">Brand Analysis and Recommendations</div>
    <p style="margin-top:8px">Strong brands command a higher valuation. We conduct a brand analysis, providing clear and detailed recommendations to enhance your value proposition and help you stand out from the crowd.</p>
    <ul class="bul">
      <li><b>Current external position among competitors --</b><br>We look at how your brand measures up based on external competitive analysis, positioning in the media and analyst community, and across other digital channels.</li>
      <li><b>Physical brand image--</b><br>A little bit of paint and updated fixtures can go a long way when increasing the value of a home. The same is true for businesses. Our audit evaluates non-disruptive steps your company can take to enhance your brand look and feel before sale.</li>
      <li><b>Employee brand perception--</b><br>We conduct a high-level external audit with recommendations to enhance engagement for current and prospective employees.</li>
      <li><b>Customer brand perception--</b><br>We conduct a high-level external audit showcasing how customers perceive your brand in the market. We then provide recommendations for enhancing engagement and maximizing value.</li>
    </ul>
  </div>
  <div class="abs" style="left:36px;top:326px;width:138px;height:116px;background:#1f6cb5;color:#fff;font-size:5.8px;font-style:italic;font-weight:600;line-height:1.4;padding:16px 8px 0">
    <p>A 5% increase in customer retention correlates with at least a 25% increase in profit, according to an analysis by Halvorsen &amp; Company.</p>
    <p style="margin-top:9px">It costs 5 times more to acquire a new customer than to retain a current one and 16 times more to get new customers to the same spending level as existing ones.</p>
  </div>
  <div class="abs brand" style="left:80px;top:500px;font-size:7px"><span class="mark"></span>BRIGHTLARKMOOR PARTNERS</div>
  <div class="abs body" style="left:206px;top:62px;width:172px">
    <div class="sec-h">Digital and Traditional Marketing Analysis and Recommendations</div>
    <p style="margin-top:8px">It's about your valuation. Full and fair valuation requires a clear, compelling investment case articulated consistently to the right audience at the right time. Messaging to maximize your value in an acquisition or an IPO is quite different from typical selling messages for prospects, customers, or features and benefits for press and analysts. We understand the issues and speak the right language to maximize perception of value with key decision makers.</p>
    <ul class="bul" style="font-style:italic">
      <li>Review and recommendations of key messaging and value proposition</li>
      <li>Analysis and recommendations to highlight data, IP, and innovation</li>
      <li>Analysis and recommendations to position key executives likely to remain with the company as thought leaders to help build value</li>
      <li>Analysis and recommendations to build employee engagement and retention enhancing your most valuable asset--your team</li>
    </ul>
    <div class="sec-h" style="margin-top:10px">Media and Analyst Strategy Development</div>
    <p style="margin-top:8px">Positive articles and inclusion in analyst reports pack a powerful punch when preparing your business for sale. We work with clients to develop a media strategy that goes beyond brand awareness, leveraging media to build a digital history of third-party validation targeted to enhance appeal to prospective buyers while generating credibility and connections to enhance overall value.</p>
    <ul class="bul" style="font-style:italic">
      <li>Positioning to media and analyst community creating third party market validation</li>
      <li>Key angle recommendations</li>
      <li>Announcement timeline and strategy planning to maximize media value of news</li>
      <li style="margin-left:8px">What is newsworthy</li>
      <li style="margin-left:8px">How to position that news for the most significant impact</li>
    </ul>
    <div class="sec-h" style="margin-top:10px">"White Hat/Black Hat Review"</div>
    <p style="margin-top:8px">We take a buyer's communications and marketing approach to analyzing the client company and provide a "punch list" of things a potential buyer is likely to ask/request in due diligence from a comms/culture/marketing/reputation standpoint to ensure that when potential buyers start screening for sellers and evaluating them, the client company has the upper hand.</p>
  </div>
</section>

<!-- Page 4 -->
<section class="page p4">
  <svg class="layer" width="390" height="552" viewBox="0 0 390 552">
    <rect x="0" y="0" width="390" height="125" fill="#1f6cb5"/>
    <polygon points="235,0 390,0 390,230 305,230 250,100" fill="#4f83c4" role="img" aria-label="Photo of a glass skyscraper against a blue sky"/>
    <polygon points="250,100 330,200 390,180 390,215 310,230" fill="#1f6cb5" opacity=".6"/>
    <polygon points="330,200 390,165 390,260" fill="#e8901c"/>
    <polygon points="0,375 0,552 390,552 390,455 330,490 200,400 90,440" fill="#cdd3d8" role="img" aria-label="Illustration of a grey and green city skyline"/>
    <polygon points="0,375 90,440 70,552 0,552" fill="#5c9e2e"/>
    <polygon points="0,530 390,505 390,552 0,552" fill="#1f6cb5"/>
  </svg>
  <div class="abs" style="left:28px;top:22px;width:210px;color:#fff;font-size:10px;font-style:italic;line-height:1.3">"Strategy without tactics is the slowest route to victory. Tactics without strategy is the noise before defeat."</div>
  <div class="abs" style="left:24px;top:80px;color:#fff;font-size:10px;font-weight:600">– Aldren Voss</div>
  <div class="abs body" style="left:24px;top:136px;width:200px;color:#333">Once the analysis is complete, we deliver actionable intelligence and recommendations to help leaders identify and quickly unlock areas that will boost value and appeal to prospective buyers. Work products include:</div>
  <ul class="abs body bul" style="left:22px;top:172px;width:222px">
    <li><b>Gap Assessment --</b><br>We provide a comprehensive seller report providing analysis and actionable recommendations to increase your valuation while identifying and mitigating non-financial risks.</li>
    <li><b>Strategic Roadmap --</b><br>Clients are given an actionable tactical roadmap based on the recommendation provided. Organizations can choose to implement key areas or include this powerful guide as part of their presentation to prospective buyers to highlight latent potential. The roadmap provides actionable steps buyers can take upon close as they make their case for your business with their investment committees.</li>
  </ul>
  <div class="abs body" style="left:24px;top:284px;width:345px;color:#333">
    <p>Once the strategy integration roadmap is complete, your team can implement it on your timeline, we can work with your team providing guidance and executive-level support, or we can fully execute deliverables with our robust capabilities and team.</p>
    <p style="margin-top:6px">Our value proposition, based on delivering outcomes rather than just outputs, means that you receive the benefit and capability of deeply experienced corporate communications leaders without adding headcount or the time to identify, recruit, onboard and retain a new team member.</p>
    <p style="margin-top:6px">We help organizations enhance their valuation by identifying areas that will appeal most to buyers and ensuring those elements of your business are visible and memorable to those who matter most.</p>
    <p style="margin-top:6px">SaleWise helps sellers maximize valuation and unlock hidden potential ahead of an exit--ensuring money is not left on the table.</p>
  </div>
  <div class="abs brand" style="left:150px;top:456px;font-size:9px"><span class="mark"></span>BRIGHTLARKMOOR PARTNERS</div>
</section>

</body>
</html>
```